Local Directory Ad

We currently have an advertisement in our local directory (see attached). We would like to make it look more appealing.
Dimensions are 110mm H X 175mm W
We would like to keep the same colours and contact details remain the same.
Most of the content can remain the same, Just remove the line Tax effective remote area salary packaging and add in Self Managed Super Funds.We want to change mortgage broking to Mortgage Broking and Loan Structuring.

We want to change the line Local accountants Local Knowledge Local Experience - to something like local knowledge beyond compare or unsurpassed local knowledge but open to suggestions on this.

there are some good designs posted so far. I particulalry like the ones from pulmawick, korbu41, and the last one posted by wexlorunti and PLV. Keep up the good work guys

```html
<!DOCTYPE html>
<html lang="en">
<head>
<meta charset="utf-8">
<title>Marlow Ridge Advisory – Directory Ad</title>
<link rel="stylesheet" href="https://fonts.googleapis.com/css2?family=Roboto+Condensed:wght@400;700&display=swap">
<style>
  :root {
    --red: #e3101f;
    --gold: #fbc311;
    --cream: #fdf6a8;
    --white: #ffffff;
    --ink: #111111;
    --tag-yellow: #fde021;
    --bullet: #f4ea1a;
    --sky: #18c1f2;
    --amber: #fcc214;
    --green: #2fe21c;
  }
  html, body {
    margin: 0;
    padding: 0;
    overflow: hidden;
    background: var(--white);
  }
  .ad {
    position: relative;
    width: 1200px;
    height: 755px;
    overflow: hidden;
    background: linear-gradient(180deg, var(--cream) 0%, #fefbd8 60%, var(--white) 100%);
    font-family: "Roboto Condensed", "Arial Narrow", sans-serif;
    color: var(--ink);
  }
  .ad__shapes {
    position: absolute;
    inset: 0;
  }
  .ad__top-band {
    position: absolute;
    top: 0; left: 0;
    width: 1200px; height: 14px;
    background: var(--gold);
  }
  .brand {
    position: absolute;
    left: 40px;
    top: 84px;
    margin: 0;
    font-weight: 700;
    font-size: 84px;
    line-height: 84px;
    color: var(--white);
  }
  .licence {
    position: absolute;
    left: 40px;
    top: 342px;
    margin: 0;
    font-size: 21px;
    color: var(--white);
  }
  .tagline {
    position: absolute;
    left: 40px;
    top: 396px;
    margin: 0;
    font-weight: 700;
    font-size: 30px;
    line-height: 36px;
    color: var(--tag-yellow);
  }
  .services-title {
    position: absolute;
    left: 752px;
    top: 62px;
    margin: 0;
    font-weight: 700;
    font-size: 30px;
    line-height: 36px;
  }
  .services-rule {
    position: absolute;
    left: 752px;
    top: 153px;
    width: 448px;
    height: 2px;
    background: var(--white);
  }
  .services {
    position: absolute;
    left: 752px;
    top: 178px;
    margin: 0;
    padding: 0;
    list-style: none;
    font-size: 23px;
    line-height: 27px;
  }
  .services li {
    position: relative;
    padding-left: 28px;
    margin-bottom: 19px;
  }
  .services li::before {
    content: "";
    position: absolute;
    left: 0;
    top: 6px;
    width: 11px;
    height: 11px;
    border-radius: 50%;
    background: var(--bullet);
  }
  .contact {
    position: absolute;
    left: 780px;
    top: 503px;
    margin: 0;
    font-style: normal;
    font-size: 21px;
    line-height: 30px;
  }
  .contact .fax { margin-left: 26px; }
  .website {
    position: absolute;
    left: 780px;
    top: 666px;
    margin: 0;
    font-weight: 700;
    font-size: 35px;
  }
</style>
</head>
<body>
<main class="ad">
  <svg class="ad__shapes" width="1200" height="755" viewBox="0 0 1200 755" aria-hidden="true">
    <g class="hero-blob" fill="var(--red)">
      <circle cx="318" cy="306" r="276"/>
      <circle cx="150" cy="150" r="220"/>
      <rect x="0" y="0" width="300" height="510"/>
      <rect x="0" y="0" width="400" height="120"/>
    </g>
  </svg>
  <div class="ad__top-band"></div>

  <svg class="ad__shapes" width="1200" height="755" viewBox="0 0 1200 755">
    <g role="img" aria-label="Icon of office binders">
      <circle cx="665" cy="394" r="75" fill="var(--sky)"/>
    </g>
    <g role="img" aria-label="Icon of a briefcase">
      <circle cx="617" cy="566" r="90" fill="var(--red)"/>
      <circle cx="617" cy="566" r="66" fill="var(--amber)"/>
    </g>
    <g role="img" aria-label="Icon of stacked coins">
      <circle cx="499" cy="667" r="50" fill="var(--red)"/>
      <circle cx="499" cy="667" r="45" fill="var(--green)"/>
    </g>
  </svg>

  <h1 class="brand">Marlow<br>Ridge<br>Advisory</h1>
  <p class="licence">Australian Credit Licence 512 884</p>
  <p class="tagline">Local knowledge beyond<br>compare or unsurpassed<br>local knowledge</p>

  <h2 class="services-title">We are here for you all year<br>round to assist with...</h2>
  <div class="services-rule"></div>
  <ul class="services">
    <li>Accounting &amp; Taxation</li>
    <li>Business Advice CST and BAS's</li>
    <li>Mortgage Broking &amp; Loan Structuring</li>
    <li>Bookkeeping</li>
    <li>Self Managed Super Funds for<br>your employees</li>
  </ul>

  <address class="contact">
    Shop 3 Harbour Arcade<br>
    12 Wattle St. Pindara<br>
    PO Box 145 Pindara 6799<br>
    reception@mradvisory.com.au<br>
    Ph: 9100 4827<span class="fax">Fax: 9100 4828</span>
  </address>
  <p class="website">www.mradvisory.com.au</p>
</main>
</body>
</html>
```